Are You Ready For The Next Hail Storm?

We need a two paged (Front and Back) flyer to educate our potential clients to what our company does.
I have included some previous pamphlets along with products we carry.
Want a info-tutorial on what we do for the clients and how they can sign up.
One page both sides type of pamphlet.
Clear steps as to how we can help them and to have the peace of mind knowing their home is protected.
Our mantra is : Happy Homes, Protected By Experts, Built By Trust.

Target Market(s)

Home Owners worried about storm events.

Industry/Entity Type

Insurance

Requirements
Must have
• (Logo Package Uploaded - 1960's feel to our company)
Home Protection Package:
Sign up today @ StormCoverPlan.com
Discount Code - STORMSAFE
We take all the worry from homeowners. Our Homeowner Hail/Wind Protection Package includes 24/7/365 monitoring of property for hail events. Emergency crews to close up any windows or roof leaks. Educational Information and Review of Current Policy.
Emergency Response: 1 - Damage triage. 2 - Mitigate Further Damage. 3 - Inspect and Assess. 4 - Deal with Insurance on Your Behalf To Maximize Your Home Claim. 5 - Restoration of Home With The Proper Funding From Your Insurance Claim.
Insurance Liaison Option.
Sign up @ www.ClaimBridgeHelp.com
www.TheRenewalMedic.com
Our Commitment:
30 minute first contact.
Onsite within hours.
Thorough documentation.
Empathy and care handling your complete claim.
Full warranty package registered on your behalf.
24/7/365 Service

PSX Registered
2 Million General Liability
Calgary Business License
Fair Trade Registry A+ Accreditation
Nice to have
• Walk the home owners through a visual and text pamphlet.

```html
<!DOCTYPE html>
<html lang="en">
<head>
<meta charset="utf-8">
<title>Home Protection Flyer – Front and Back</title>
<link rel="stylesheet" href="https://fonts.googleapis.com/css2?family=Montserrat:wght@400;500;600;700;800&family=Barlow+Semi+Condensed:wght@600;700&display=swap">
<style>
:root{
  --teal:#5bbfb5;
  --orange:#f8ad5e;
  --ink:#2b2f31;
  --red:#e02020;
  --panel:#efefef;
  --line:#d9d9d9;
  --backdrop:#f1e4da;
  --white:#ffffff;
}
*{box-sizing:border-box;margin:0;padding:0}
html,body{width:814px;height:1200px;overflow:hidden;background:var(--backdrop)}
body{position:relative;font-family:"Montserrat",sans-serif;color:var(--ink)}
.sheet-slot{position:absolute;top:331px;width:380px;height:538px;overflow:hidden;box-shadow:0 6px 18px rgba(0,0,0,.12)}
.sheet-slot.front{left:18px}
.sheet-slot.back{left:416px}
.page{position:absolute;left:0;top:0;width:694px;height:982px;background:var(--white);transform:scale(.5476);transform-origin:0 0;overflow:hidden}
.shapes{position:absolute;left:0;top:0;width:694px;height:982px}
.brand-name{position:absolute;left:48px;top:78px;font-weight:800;font-size:24px;color:var(--ink);display:flex;align-items:center;gap:8px;white-space:nowrap}
.brand-name i{display:block;width:14px;height:14px;border-radius:50%;background:var(--orange)}
.headline{position:absolute;left:42px;top:308px;font-weight:800;font-size:29px;line-height:33px;letter-spacing:.6px;color:var(--ink)}
.headline .light{color:var(--white)}
.tab{position:absolute;background:var(--orange);color:var(--white);font-weight:700;text-align:center;border-radius:22px 22px 0 0}
.package-tab{left:198px;top:470px;width:304px;height:50px;font-size:19px;line-height:19px;padding-top:5px}
.rule{position:absolute;left:55px;top:520px;width:590px;height:1px;background:var(--line)}
.client{position:absolute;top:546px;width:215px}
.client h3{font-size:14px;line-height:17px;font-weight:700;color:var(--teal);margin-bottom:14px}
.ticks{list-style:none}
.ticks li{position:relative;padding-left:17px;font-size:9px;line-height:20px;font-weight:500;white-space:nowrap}
.ticks li::before{content:"";position:absolute;left:0;top:6px;width:9px;height:9px;border-radius:50%;background:var(--orange)}
.ticks li::after{content:"";position:absolute;left:3px;top:8px;width:2px;height:4px;border:solid var(--white);border-width:0 1.4px 1.4px 0;transform:rotate(45deg)}
.ticks.teal li::before{background:var(--teal)}
.signup-small{position:absolute;left:42px;top:698px;font-size:16px;font-weight:700}
.signup-small span,.accent{color:var(--teal)}
.url-box{position:absolute;left:42px;top:728px;width:250px;height:40px;background:var(--orange);font-size:17px;font-weight:700;line-height:40px;padding-left:10px;white-space:nowrap}
.code-box{position:absolute;left:310px;top:690px;width:176px;height:84px;border:2px dashed #9a9a9a;border-radius:10px;box-shadow:0 2px 4px rgba(0,0,0,.15)}
.code-box .label{position:absolute;left:8px;top:10px;font-size:12.5px;font-weight:700;display:flex;white-space:nowrap}
.code-box .label b{background:var(--orange);padding:5px 8px}
.code-box .label em{font-style:normal;color:var(--teal);padding:5px 8px}
.code-box .code{position:absolute;left:0;right:0;top:48px;text-align:center;font-size:16px;font-weight:600}
.blurb{position:absolute;left:40px;top:800px;width:372px;font-size:11px;line-height:14px}
.mascot{position:absolute}
.contact{position:absolute;left:42px;top:925px;display:flex;align-items:center;font-family:"Barlow Semi Condensed",sans-serif;font-weight:700;white-space:nowrap}
.contact .label{font-size:22px;letter-spacing:.5px;margin-right:16px}
.contact svg{margin-right:6px}
.contact .number{font-size:29px}
.resp-tab{position:absolute;left:30px;top:322px;width:355px;height:42px;background:var(--teal);border-radius:22px;color:var(--white);font-size:20px;font-weight:700;line-height:42px;padding-left:24px;box-shadow:-4px 5px 0 var(--ink)}
.resp-panel{position:absolute;left:40px;top:352px;width:615px;height:212px;background:var(--panel)}
.resp-divider{position:absolute;left:330px;top:383px;width:1px;height:170px;background:#c8c8c8}
.step{position:absolute;display:flex;align-items:center;font-size:11px;font-weight:700;line-height:14px}
.step svg{flex:none;margin-right:18px}
.step p{width:210px}
.signup{position:absolute;left:42px;top:593px;font-size:21px;font-weight:700}
.urls{position:absolute;left:42px;top:628px;font-size:18px;line-height:24px;font-weight:700;white-space:nowrap}
.service{position:absolute;left:405px;top:588px;width:150px;height:150px}
.service svg{position:absolute;left:0;top:0}
.service .big{position:absolute;left:0;width:144px;top:52px;text-align:center;font-size:40px;line-height:40px;font-weight:500;letter-spacing:-1px}
.service .small{position:absolute;left:0;width:144px;top:94px;text-align:center;font-size:15px;line-height:16px;font-weight:700}
.commit-title{position:absolute;left:42px;top:698px;font-size:21px;font-weight:700}
.commit{position:absolute;left:42px;top:730px}
.commit li{font-size:10px;line-height:13px;font-weight:700}
.commit li::before{top:2px}
.commit li::after{top:4px}
.partners{position:absolute;left:42px;top:820px;display:flex;align-items:center;gap:30px}
.partner-name{font-size:16px;font-weight:800;display:flex;align-items:center;gap:6px;white-space:nowrap}
.partner-name i{display:block;width:12px;height:12px;background:var(--ink)}
.partner-name i.round{border-radius:50%;background:var(--teal)}
.seal{width:72px;height:52px;background:#1f5ea8;border-radius:4px}
</style>
</head>
<body>

<div class="sheet-slot front">
<section class="page">
  <svg class="shapes" viewBox="0 0 694 982">
    <defs>
      <linearGradient id="houseSky" x1="0" y1="0" x2="0" y2="1">
        <stop offset="0" stop-color="#dfe9f1"/><stop offset=".55" stop-color="#e9e9e6"/><stop offset="1" stop-color="#8a8d8e"/>
      </linearGradient>
      <linearGradient id="mascotTone" x1="0" y1="0" x2="1" y2="1">
        <stop offset="0" stop-color="#f3d37a"/><stop offset=".5" stop-color="#7fc9ae"/><stop offset="1" stop-color="#2f3a5a"/>
      </linearGradient>
    </defs>
    <polygon role="img" aria-label="Photo of a modern white two-storey house with dark roof under a cloudy sky" points="0,0 694,0 694,390 600,372 0,220" fill="url(#houseSky)"/>
    <polygon points="425,0 694,0 694,80" fill="var(--teal)"/>
    <polygon points="0,220 606,370 0,468" fill="var(--teal)"/>
    <polygon points="0,900 470,900 435,982 0,982" fill="var(--orange)"/>
    <polygon points="455,935 694,935 694,982 435,982" fill="var(--teal)"/>
  </svg>

  <div class="brand-name"><i></i>The Renewal Medic</div>

  <h1 class="headline">HAPPY HOMES,<br>PROTECTED BY EXPERTS,<br><span class="light">BUILT BY TRUST</span></h1>

  <div class="tab package-tab">HOME PROTECTION<br>PACKAGE:</div>
  <div class="rule"></div>

  <div class="client" style="left:42px">
    <h3>CLIENT #1<br>CITYSCAPE NORTH EAST</h3>
    <ul class="ticks">
      <li>Initial Insurance Offer : &nbsp;$3,205.53</li>
      <li>Our Approved Estimate: &nbsp;$27,101.68</li>
      <li>Approved Estimate: &nbsp;$27,101.68</li>
    </ul>
  </div>
  <div class="client" style="left:257px">
    <h3>CLIENT #2<br>NEW BRIGHTEN DR SE</h3>
    <ul class="ticks">
      <li>Initial Insurance Offer : &nbsp;$3,777.90</li>
      <li>Our Approved Estimate: &nbsp;$36,350.79</li>
      <li>INCREASE OF - $ 32,572.89</li>
    </ul>
  </div>
  <div class="client" style="left:460px">
    <h3>CLIENT #3<br>SKYVIEW SHORES M NE</h3>
    <ul class="ticks">
      <li>Initial Insurance Offer : &nbsp;$44,753.50</li>
      <li>Our Approved Estimate: &nbsp;$ 69,235.59</li>
      <li>INCREASE OF - $ 24,482.09</li>
    </ul>
  </div>

  <div class="signup-small">SIGN UP <span>TODAY</span></div>
  <div class="url-box">@ StormCoverPlan.com</div>

  <div class="code-box">
    <div class="label"><b>DISCOUNT</b><em>CODE</em></div>
    <div class="code">STORMSAFE</div>
  </div>

  <p class="blurb">We take all the worry from homeowners. Our Homeowner Hail/Wind Protection Package includes 24/7/365 monitoring of property for hail events. Emergency crews to close up any windows or roof leaks. Educational Information and Review of Current Policy.</p>

  <svg class="mascot" style="left:505px;top:672px" width="165" height="290" viewBox="0 0 165 290">
    <rect role="img" aria-label="Cartoon mascot of a friendly doctor in a white coat holding a clipboard and giving a thumbs up" width="165" height="290" rx="36" fill="url(#mascotTone)" opacity=".85"/>
  </svg>

  <div class="contact">
    <span class="label">CONTACT US</span>
    <svg width="22" height="22" viewBox="0 0 22 22"><circle cx="11" cy="11" r="11" fill="var(--orange)"/><path d="M7 5.5c.6-.4 1.3-.3 1.6.3l1 2c.2.5.1 1-.3 1.3l-.8.6c.6 1.4 1.6 2.4 3 3l.6-.8c.3-.4.9-.5 1.3-.3l2 1c.6.3.7 1 .3 1.6l-.7 1c-.5.6-1.3.8-2 .5-3.2-1.2-5.5-3.5-6.7-6.7-.3-.7-.1-1.5.5-2z" fill="var(--white)"/></svg>
    <span class="number">1-403-555-0148</span>
  </div>
</section>
</div>

<div class="sheet-slot back">
<section class="page">
  <svg class="shapes" viewBox="0 0 694 982">
    <defs>
      <linearGradient id="villaTone" x1="0" y1="0" x2="0" y2="1">
        <stop offset="0" stop-color="#dbe6ee"/><stop offset=".35" stop-color="#c9643e"/><stop offset=".6" stop-color="#e2b45e"/><stop offset="1" stop-color="#5f9a3c"/>
      </linearGradient>
      <linearGradient id="mascotTone2" x1="0" y1="0" x2="1" y2="1">
        <stop offset="0" stop-color="#f3d37a"/><stop offset=".5" stop-color="#7fc9ae"/><stop offset="1" stop-color="#2f3a5a"/>
      </linearGradient>
    </defs>
    <polygon role="img" aria-label="Photo of a single-storey yellow villa with a red tiled roof, green lawn and garden" points="0,0 694,0 694,338 300,236 0,170" fill="url(#villaTone)"/>
    <polygon points="590,0 694,0 694,28" fill="var(--orange)"/>
    <polygon points="0,170 300,236 0,298" fill="var(--orange)"/>
    <polygon points="0,900 470,900 440,982 0,982" fill="var(--orange)"/>
    <polygon points="458,935 694,935 694,982 440,982" fill="var(--teal)"/>
  </svg>

  <div class="resp-panel"></div>
  <div class="resp-tab">EMERGENCY RESPONSE:</div>
  <div class="resp-divider"></div>

  <div class="step" style="left:75px;top:386px">
    <svg width="40" height="40" viewBox="0 0 40 40"><circle cx="20" cy="20" r="18" fill="var(--white)" stroke="var(--teal)" stroke-dasharray="3 3"/><rect x="13" y="13" width="14" height="14" fill="none" stroke="var(--ink)" stroke-width="1.5"/><path d="M16 24l4-5 3 3" fill="none" stroke="var(--ink)" stroke-width="1.5"/></svg>
    <p>DAMAGE <span class="accent">TRIAGE</span></p>
  </div>
  <div class="step" style="left:75px;top:446px">
    <svg width="40" height="40" viewBox="0 0 40 40"><circle cx="20" cy="20" r="18" fill="var(--white)" stroke="var(--teal)" stroke-dasharray="3 3"/><circle cx="20" cy="15" r="3" fill="var(--ink)"/><path d="M14 28v-5h12v5M17 23v5M23 23v5" fill="none" stroke="var(--ink)" stroke-width="1.6"/></svg>
    <p>MITIGATE <span class="accent">FURTHER DAMAGE</span></p>
  </div>
  <div class="step" style="left:75px;top:504px">
    <svg width="40" height="40" viewBox="0 0 40 40"><circle cx="20" cy="20" r="18" fill="var(--white)" stroke="var(--teal)" stroke-dasharray="3 3"/><circle cx="22" cy="17" r="5" fill="none" stroke="var(--ink)" stroke-width="1.8"/><path d="M18.5 20.5l-6 6" stroke="var(--ink)" stroke-width="2.2"/></svg>
    <p>INSPECT AND <span class="accent">ASSESS.</span></p>
  </div>
  <div class="step" style="left:345px;top:386px">
    <svg width="40" height="40" viewBox="0 0 40 40"><circle cx="20" cy="20" r="18" fill="var(--white)" stroke="var(--teal)" stroke-dasharray="3 3"/><path d="M13 20a7 7 0 1 0 2-5" fill="none" stroke="var(--ink)" stroke-width="1.8"/><path d="M12 12v4h4" fill="none" stroke="var(--ink)" stroke-width="1.8"/><circle cx="20" cy="20" r="1.6" fill="var(--ink)"/></svg>
    <p>DEAL WITH INSURANCE ON YOUR <span class="accent">BEHALF TO MAXIMIZE YOUR HOME CLAIM</span></p>
  </div>
  <div class="step" style="left:345px;top:446px">
    <svg width="40" height="40" viewBox="0 0 40 40"><circle cx="20" cy="20" r="18" fill="var(--white)" stroke="var(--teal)" stroke-dasharray="3 3"/><path d="M20 10l8 3v6c0 5-3.5 8.5-8 10-4.5-1.5-8-5-8-10v-6z" fill="var(--ink)"/><path d="M16.5 19.5l2.5 2.5 4.5-5" fill="none" stroke="var(--white)" stroke-width="1.8"/></svg>
    <p>RESTORATION OF HOME WITH THE <span class="accent">PROPER FUNDING FROM YOUR INSURANCE CLAIM.</span></p>
  </div>
  <div class="step" style="left:345px;top:504px">
    <svg width="40" height="40" viewBox="0 0 40 40"><circle cx="20" cy="20" r="18" fill="var(--white)" stroke="var(--teal)" stroke-dasharray="3 3"/><path d="M20 10l8 3v6c0 5-3.5 8.5-8 10-4.5-1.5-8-5-8-10v-6z" fill="var(--ink)"/><path d="M16.5 19.5l2.5 2.5 4.5-5" fill="none" stroke="var(--white)" stroke-width="1.8"/></svg>
    <p>INSURANCE <span class="accent">LIAISON OPTION</span></p>
  </div>

  <div class="signup">SIGN UP <span class="accent">TODAY</span></div>
  <div class="urls">@ www.ClaimBridgeHelp.com<br>www.TheRenewalMedic.com</div>

  <div class="service">
    <svg width="150" height="150" viewBox="0 0 150 150">
      <path d="M72 24A56 56 0 1 0 128 80" fill="none" stroke="var(--red)" stroke-width="4"/>
      <path d="M128 80A56 56 0 0 0 98 30" fill="none" stroke="var(--red)" stroke-width="8"/>
      <polygon points="104,14 82,28 106,42" fill="var(--red)"/>
    </svg>
    <div class="big">24/7</div>
    <div class="small">SERVICE</div>
  </div>

  <div class="commit-title">OUR <span class="accent">COMMITMENT:</span></div>
  <ul class="ticks teal commit">
    <li>30 minute first contact.</li>
    <li>Onsite within hours.</li>
    <li>Thorough documentation.</li>
    <li>Empathy and care handling your complete claim.</li>
    <li>Full warranty package registered on your behalf.</li>
  </ul>

  <div class="partners">
    <div class="partner-name"><i class="round"></i>Oakridge Roofing</div>
    <div class="seal" role="img" aria-label="Fair Trade Registry accreditation badge"></div>
    <div class="partner-name"><i></i>PSX</div>
  </div>

  <svg class="mascot" style="left:505px;top:745px" width="160" height="215" viewBox="0 0 160 215">
    <rect role="img" aria-label="Cartoon mascot of a friendly doctor in a white coat holding a clipboard and giving a thumbs up" width="160" height="215" rx="34" fill="url(#mascotTone2)" opacity=".85"/>
  </svg>

  <div class="contact">
    <span class="label">CONTACT US</span>
    <svg width="22" height="22" viewBox="0 0 22 22"><circle cx="11" cy="11" r="11" fill="var(--orange)"/><path d="M7 5.5c.6-.4 1.3-.3 1.6.3l1 2c.2.5.1 1-.3 1.3l-.8.6c.6 1.4 1.6 2.4 3 3l.6-.8c.3-.4.9-.5 1.3-.3l2 1c.6.3.7 1 .3 1.6l-.7 1c-.5.6-1.3.8-2 .5-3.2-1.2-5.5-3.5-6.7-6.7-.3-.7-.1-1.5.5-2z" fill="var(--white)"/></svg>
    <span class="number">1-403-555-0148</span>
  </div>
</section>
</div>

</body>
</html>
```